Quenby Bespoke Furnishings logo and business card

Quenby is a female operated furniture design and reupholstery business. Working with luxury top end fabrics and furnishings for unique and stylish one off designs. Bringing loved pieces of furniture back to life by recovering on modern, trendy, stylish fabrics. Think Velvet chaise lounge or velour Chesterfield lounges, vibrant and unique colourful, individually designed statement pieces.
We would like a simple logo that can be used on socials and a business card that is simple yet striking . Possibly using a bronze or gold foil.
The business name is QUENBY BESPOKE FURNISHINGS
Can be just QUENBY
Logo will be used on socials and images of finished furniture.

Target Market(s)

high end luxury holiday houses. Artistic flair designer houses

Industry/Entity Type

Home Furniture

Contact Information for Business Card

Simple yet designer
Logo on the front and name details on the back

Font styles to use
Decorative

Requirements
Must have
• Finess
A feel of artistic design
Just a logo/business name on the front of the card
Should not have
• not a picture of furniture

```html
<!DOCTYPE html>
<html lang="en">
<head>
<meta charset="utf-8">
<title>Quenby Bespoke Furnishings – Business Card</title>
<link href="https://fonts.googleapis.com/css2?family=Josefin+Sans:wght@300;400;600&family=Nunito:wght@800&display=swap" rel="stylesheet">
<style>
  :root {
    --stage: #2a2829;
    --card-dark: #1c1a1b;
    --card-dark-edge: #2e2b2c;
    --card-light: #f4f4f4;
    --ink: #2b2a2b;
    --ink-soft: #3a393a;
    --paper-text: #e6e6e6;
    --accent: #e0242c;
  }
  * { margin: 0; padding: 0; box-sizing: border-box; }
  html, body { width: 1200px; height: 900px; overflow: hidden; }
  body {
    background: var(--stage);
    display: flex;
    flex-direction: column;
    align-items: center;
    justify-content: center;
    gap: 56px;
    font-family: "Josefin Sans", sans-serif;
  }
  .card {
    width: 620px;
    height: 354px;
    border-radius: 4px;
    position: relative;
    overflow: hidden;
    box-shadow: 0 14px 30px rgba(0,0,0,.45);
  }

  /* Front */
  .card--front {
    background: linear-gradient(160deg, var(--card-dark-edge), var(--card-dark) 60%);
    display: flex;
    align-items: center;
    justify-content: center;
  }
  .wordmark {
    display: flex;
    align-items: center;
    gap: 22px;
  }
  .wordmark__square {
    width: 34px;
    height: 34px;
    background: var(--accent);
  }
  .wordmark__text {
    font-weight: 600;
    line-height: 1;
  }
  .wordmark__name {
    display: block;
    font-size: 78px;
    letter-spacing: 1px;
  }
  .wordmark__tagline {
    display: block;
    font-size: 17px;
    letter-spacing: 3px;
    margin-top: 8px;
  }
  .card--front .wordmark__text { color: var(--paper-text); }

  /* Back */
  .card--back {
    background: linear-gradient(150deg, #ffffff, var(--card-light) 55%, #e9e9e9);
    display: flex;
    align-items: center;
  }
  .card--back .brand {
    width: 48%;
    display: flex;
    justify-content: center;
  }
  .card--back .wordmark { gap: 14px; }
  .card--back .wordmark__square { width: 22px; height: 22px; }
  .card--back .wordmark__name { font-size: 54px; }
  .card--back .wordmark__tagline { font-size: 12px; letter-spacing: 2px; margin-top: 6px; }
  .card--back .wordmark__text { color: var(--ink); }

  .details {
    flex: 1;
    padding-left: 14px;
    color: var(--ink-soft);
  }
  .person__name {
    font-family: "Nunito", sans-serif;
    font-weight: 800;
    font-size: 27px;
    color: var(--accent);
    margin-left: 36px;
  }
  .person__role {
    font-weight: 300;
    font-size: 15px;
    letter-spacing: 1px;
    margin-left: 36px;
    margin-top: 2px;
  }
  .rule {
    height: 2px;
    background: var(--accent);
    margin: 14px 0 16px;
  }
  .address {
    font-style: normal;
    font-weight: 300;
    font-size: 15px;
    line-height: 1.4;
    letter-spacing: 1px;
    margin-left: 26px;
  }
  .contacts {
    list-style: none;
    margin-top: 12px;
    font-weight: 300;
    font-size: 14px;
    letter-spacing: .6px;
  }
  .contacts li {
    display: flex;
    align-items: center;
    gap: 10px;
    line-height: 1.6;
  }
  .contacts svg { width: 14px; height: 14px; flex: none; }
  .contacts .domain { color: var(--accent); }
</style>
</head>
<body>

  <section class="card card--front" aria-label="Card front">
    <div class="wordmark">
      <span class="wordmark__square"></span>
      <span class="wordmark__text">
        <span class="wordmark__name">Quenby</span>
        <span class="wordmark__tagline">BESPOKE FURNISHINGS</span>
      </span>
    </div>
  </section>

  <section class="card card--back" aria-label="Card back">
    <div class="brand">
      <div class="wordmark">
        <span class="wordmark__square"></span>
        <span class="wordmark__text">
          <span class="wordmark__name">Quenby</span>
          <span class="wordmark__tagline">BESPOKE FURNISHINGS</span>
        </span>
      </div>
    </div>

    <div class="details">
      <p class="person__name">Mara Ellison</p>
      <p class="person__role">Owner</p>
      <div class="rule"></div>
      <address class="address">218 Linden Hollow Lane<br>Brookfield, OH 44403</address>
      <ul class="contacts">
        <li>
          <svg viewBox="0 0 14 14" aria-hidden="true"><circle cx="7" cy="7" r="7" fill="#e0242c"/><path d="M4.3 4.2c.5-.5 1-.4 1.3.1l.6 1c.2.4 0 .7-.3.9l-.3.2c.4.9 1 1.5 1.9 1.9l.2-.3c.2-.3.5-.5.9-.3l1 .6c.5.3.6.8.1 1.3-.8.8-2.3.5-3.8-1S3.5 5 4.3 4.2z" fill="#fff"/></svg>
          555 014 27 63
        </li>
        <li>
          <svg viewBox="0 0 14 14" aria-hidden="true"><circle cx="7" cy="7" r="7" fill="#e0242c"/><rect x="3.5" y="4.5" width="7" height="5" fill="none" stroke="#fff" stroke-width=".9"/><path d="M3.5 4.6 7 7.3l3.5-2.7" fill="none" stroke="#fff" stroke-width=".9"/></svg>
          info@quenbyfurniture.com
        </li>
        <li>
          <svg viewBox="0 0 14 14" aria-hidden="true"><circle cx="7" cy="7" r="7" fill="#e0242c"/><circle cx="7" cy="7" r="3.6" fill="none" stroke="#fff" stroke-width=".9"/><path d="M3.4 7h7.2M7 3.4c-1.4 1.8-1.4 5.4 0 7.2M7 3.4c1.4 1.8 1.4 5.4 0 7.2" fill="none" stroke="#fff" stroke-width=".8"/></svg>
          <span>www.<span class="domain">quenbyfurniture</span>.com</span>
        </li>
      </ul>
    </div>
  </section>

</body>
</html>
```